New Business Card Design*

We are a recruitment company based in Norwich/Cambridge England.
I have included our company logo which we want to remain the same.

What we are looking for is a new creative Business card which will really stand out!!

Contact Information for Business Card

Harriet Vance
email: Harriet@brelvix.co.uk
Address: Tolworth House
Ashgrove Innovation Park
Pelham Road
Norwich
KT9 3QD
Tel:01632 960418

```html
<!DOCTYPE html>
<html lang="en">
<head>
<meta charset="utf-8">
<title>Brelvix Business Card</title>
<link rel="stylesheet" href="https://fonts.googleapis.com/css2?family=Open+Sans:wght@400;600&display=swap">
<style>
  :root {
    --page: #ece9e4;
    --card: #ffffff;
    --green: #8cc63f;
    --grey: #939598;
    --text-light: #ffffff;
  }
  html, body {
    margin: 0;
    padding: 0;
    width: 1200px;
    height: 886px;
    overflow: hidden;
    background: var(--page);
  }
  .canvas {
    position: relative;
    width: 1200px;
    height: 886px;
    display: flex;
    align-items: center;
    justify-content: center;
    gap: 120px;
  }
  .card {
    width: 360px;
    height: 620px;
    background: var(--card);
    box-shadow: 0 6px 18px rgba(0,0,0,0.18);
  }
  .card svg { display: block; }
  .brand-name {
    font-family: 'Open Sans', sans-serif;
    font-weight: 600;
    fill: var(--green);
  }
  .contact {
    font-family: 'Open Sans', sans-serif;
    fill: var(--text-light);
  }
  .contact-name { font-size: 18px; font-weight: 400; letter-spacing: 0.5px; }
  .contact-role { font-size: 13px; letter-spacing: 0.5px; }
  .contact-line { font-size: 13px; }
  .brand-dot { fill: var(--grey); }
  .shape-green { fill: var(--green); }
  .shape-grey { fill: var(--grey); }
  .icon { fill: var(--text-light); }
</style>
</head>
<body>
<main class="canvas">

  <section class="card card-front" aria-label="Business card front">
    <svg width="360" height="620" viewBox="0 0 360 620">
      <g class="brand-lockup">
        <circle class="brand-dot" cx="150" cy="80" r="14"/>
        <text class="brand-name" x="174" y="92" font-size="34">Brelvix</text>
      </g>

      <path class="shape-green" role="img" aria-label="Decorative green colour field"
            d="M0,230 Q180,170 360,200 L360,365 Q70,385 28,596 L0,596 Z"/>
      <path class="shape-grey" d="M40,620 Q60,400 360,380 L360,620 Z"/>

      <g class="contact" transform="translate(150,604) rotate(-90)">
        <text class="contact-name" x="0" y="0">HARRIET VANCE</text>
        <text class="contact-role" x="0" y="20">CEO/FOUNDER</text>

        <text class="contact-line" x="0" y="50">Tolworth House</text>
        <text class="contact-line" x="0" y="68">Ashgrove Innovation Park</text>
        <text class="contact-line" x="0" y="86">Pelham Road</text>
        <text class="contact-line" x="0" y="104">Norwich KT9 3QD</text>

        <g class="icon" transform="translate(0,124)">
          <path d="M1,-9 L4,-10 L6,-6 L4,-4.5 Q5.5,-1.5 8.5,0 L10,-2 L13,0 L12,3 Q4,3 1,-9 Z"/>
        </g>
        <text class="contact-line" x="20" y="134">01632 960418</text>

        <g class="icon" transform="translate(0,142)">
          <rect x="0" y="0" width="13" height="10" rx="1"/>
          <path d="M0.5,0.5 L6.5,5.5 L12.5,0.5" fill="none" stroke="#939598" stroke-width="1.2"/>
        </g>
        <text class="contact-line" x="20" y="152">Harriet@brelvix.co.uk</text>

        <g class="icon" transform="translate(6.5,165)">
          <circle r="6.5"/>
          <ellipse rx="2.8" ry="6.5" fill="none" stroke="#939598" stroke-width="1"/>
          <line x1="-6.5" y1="0" x2="6.5" y2="0" stroke="#939598" stroke-width="1"/>
        </g>
        <text class="contact-line" x="20" y="170">www.brelvix.co.uk</text>
      </g>
    </svg>
  </section>

  <section class="card card-back" aria-label="Business card back">
    <svg width="360" height="620" viewBox="0 0 360 620">
      <g class="brand-lockup" transform="translate(180,310) rotate(90)">
        <circle class="brand-dot" cx="-86" cy="-12" r="18"/>
        <text class="brand-name" x="-58" y="4" font-size="44">Brelvix</text>
      </g>
    </svg>
  </section>

</main>
</body>
</html>
```